Lumaform website scandinavian interior design

Existing website: http://lumaform-example.no/

Webdesign for interior designer Ragna Tvedtholm. The company name is Lumaform. Scandinavian interiør is known to be simple and elegant. The website will be in Norwegian, we are working on the text. The website needs to have a few more pages than just the front page. Here are the different titles of the pages:

1. Hjem
2. Om Lumaform
3. Tjenester og priser
4.. Kontakt oss

There should be Facebook and Instagram icons somewhere at the bottom of the website.

The logo we want to use is attached (pink with black print, see attachment )

We have attached images for inspiration. We want to use some of these colors. The color in the logo, The style should be elegant, modern and delicate.

It is imprtant that the website is user friendly.

Target Market(s)

People who want to decorate their home
Companies and public sector who need to redecorate

Industry/Entity Type

Interior Designer

Coding

Coded - Design and coding required

Number of Pages Required

5+ page

Font styles to use
Other font styles liked:
• see example in the logo breakdown

Requirements
Must have
• Elegant, modern and delicate design
Images of design, see examples attached
Colors similar to the pictures
Should not have
• Too bright colors
Pictures of people

```html
<!DOCTYPE html>
<html lang="no">
<head>
<meta charset="utf-8">
<title>Lumaform – Farge &amp; Interiørdesign</title>
<link href="https://fonts.googleapis.com/css2?family=Cinzel:wght@400&family=Cormorant+Garamond:ital,wght@0,400;1,400&family=Great+Vibes&family=Lato:wght@300;400;700&display=swap" rel="stylesheet">
<style>
:root{
  --pink:#ecd3cc;
  --ink:#2f2424;
  --text:#5b5050;
  --muted:#8a8080;
  --grey:#e7e6e4;
  --line:#ffffff;
  --accent:#4a1f22;
  --white:#ffffff;
}
*{box-sizing:border-box;margin:0;padding:0}
html,body{width:1200px;height:3640px;overflow:hidden}
body{position:relative;background:var(--white);font-family:'Lato',sans-serif;color:var(--text)}
.abs{position:absolute}
.heading{font-family:'Cinzel',serif;color:var(--ink);font-weight:400;letter-spacing:2px;line-height:1.25}
.body-text{font-size:15px;line-height:1.75;color:var(--text)}
.btn{display:inline-block;border:1px solid var(--ink);padding:11px 20px;font-size:13px;letter-spacing:1.5px;color:var(--ink);font-family:'Lato',sans-serif;background:transparent;text-transform:uppercase}

/* header */
.header-band{left:0;top:0;width:1200px;height:410px;background:var(--pink)}
.nav{top:70px;font-family:'Cinzel',serif;font-size:15px;letter-spacing:1.5px;color:var(--ink)}
.brand{left:450px;top:18px;width:300px;text-align:center}
.brand-name{font-family:'Cormorant Garamond',serif;font-size:58px;color:var(--ink);line-height:1}
.brand-tag{font-family:'Cormorant Garamond',serif;font-size:12px;letter-spacing:3px;color:var(--ink);margin-top:8px}
.brand-mark{width:14px;height:14px;border:1px solid var(--ink);border-radius:50%;margin:0 auto 10px}

.hero-photo{left:140px;top:180px;width:920px;height:580px;background:linear-gradient(160deg,#efe7df 0%,#d9cdc1 45%,#b99c84 100%)}
.hero-title{left:140px;top:330px;width:920px;text-align:center;font-family:'Great Vibes',cursive;font-size:78px;color:var(--white);line-height:1.05}
.hero-btn{left:500px;top:548px;width:200px;text-align:center;border-color:var(--white);color:var(--white)}
.dots{left:570px;top:698px;display:flex;gap:8px}
.dots span{width:9px;height:9px;border-radius:50%;background:rgba(255,255,255,.6)}
.dots span.on{background:var(--white)}

/* welcome */
.welcome-script{left:500px;top:820px;font-family:'Great Vibes',cursive;font-size:44px;color:#b8a4a0}
.welcome-heading{left:112px;top:885px;width:500px;font-size:32px}
.welcome-text{left:668px;top:838px;width:420px}
.welcome-btn{left:668px;top:1050px}

/* private */
.private-panel{left:548px;top:1188px;width:652px;height:572px;background:var(--grey)}
.private-photo{left:560px;top:1290px;width:600px;height:470px;background:linear-gradient(150deg,#f4f1ec 0%,#e3d9cf 50%,#c89c74 100%)}
.private-heading{left:112px;top:1270px;font-size:34px}
.private-text{left:112px;top:1330px;width:400px;font-size:14px;line-height:1.7}
.private-btn{left:112px;top:1655px}

/* business */
.biz-band{left:0;top:1880px;width:600px;height:640px;background:var(--pink)}
.biz-photo{left:105px;top:2010px;width:560px;height:450px;background:linear-gradient(170deg,#c9c6c2 0%,#b5b1ab 55%,#8b8782 100%)}
.biz-heading{left:712px;top:1962px;font-size:34px}
.biz-text{left:712px;top:2022px;width:420px;font-size:14px;line-height:1.7}
.biz-btn{left:712px;top:2340px}

/* testimonials */
.testi-band{left:0;top:2620px;width:1200px;height:480px;background:linear-gradient(90deg,#ebe9e6 0%,#ebe9e6 45%,#e2dfdb 100%)}
.testi-photo{left:600px;top:2620px;width:600px;height:480px;background:linear-gradient(180deg,#f2f1ef 0%,#e3e0dc 60%,#c9c2ba 100%)}
.quote-mark{left:40px;top:2640px;font-family:'Cormorant Garamond',serif;font-size:320px;color:rgba(255,255,255,.7);line-height:1}
.testi-heading{left:112px;top:2740px;font-size:34px}
.testi-text{left:112px;top:2810px;width:480px;font-size:14px;font-style:italic;line-height:1.75;color:var(--muted)}
.avatar{left:112px;top:2975px;width:110px;height:110px;border-radius:50%;background:linear-gradient(160deg,#d8d2cc,#9f968e);border:4px solid var(--white)}
.client-name{left:270px;top:3005px;font-family:'Cinzel',serif;font-size:15px;color:var(--ink);letter-spacing:1px}
.client-role{left:270px;top:3030px;font-size:13px;color:var(--muted)}
.arrows{left:530px;top:3040px;display:flex;gap:14px}

/* footer */
.footer-brand{left:110px;top:3170px;width:260px}
.footer-brand .brand-name{font-size:56px;text-align:center}
.footer-brand .brand-tag{text-align:center}
.footer-about{left:110px;top:3340px;width:320px;font-size:13px;line-height:1.6}
.foot-col{top:3210px}
.foot-title{font-family:'Cinzel',serif;font-size:15px;letter-spacing:1.5px;color:var(--ink);margin-bottom:16px}
.foot-list{list-style:none;font-size:13px;line-height:1.9;color:var(--text)}
.foot-note{font-size:13px;line-height:1.6;width:240px}
.email-field{margin-top:24px;width:250px;border:1px solid #cfc7c5;height:38px;display:flex;align-items:center;padding-left:12px;gap:10px;font-size:13px;color:var(--muted)}
.signup-btn{margin-top:18px;background:var(--accent);color:var(--white);font-size:12px;letter-spacing:1.5px;padding:10px 18px;display:inline-block}
.contact-row{display:flex;gap:12px;font-size:13px;line-height:1.5;margin-bottom:22px;width:240px}
.bottom-bar{left:0;top:3540px;width:1200px;height:100px;background:var(--pink)}
.copyright{left:110px;top:3580px;font-size:13px;color:var(--text)}
.social{left:900px;top:3568px;display:flex;gap:14px}
.social span{width:40px;height:40px;border-radius:50%;border:1px solid var(--ink)}
</style>
</head>
<body>

<div class="abs header-band"></div>
<div class="abs hero-photo" role="img" aria-label="Lyst skandinavisk interiør med spisebord, stoler og planter"></div>
<svg class="abs" style="left:0;top:0" width="1200" height="800" aria-hidden="true">
  <polyline points="128,770 128,300 470,60" fill="none" stroke="var(--line)" stroke-width="2"/>
  <polyline points="730,60 1072,300 1072,770 128,770" fill="none" stroke="var(--line)" stroke-width="2"/>
</svg>
<nav>
  <span class="abs nav" style="left:170px">HJEM</span>
  <span class="abs nav" style="left:330px">OM LUMAFORM</span>
  <span class="abs nav" style="left:780px">TJENESTER OG PRISER</span>
  <span class="abs nav" style="left:1040px">KONTAKT OSS</span>
</nav>
<div class="abs brand">
  <div class="brand-mark"></div>
  <div class="brand-name">Lumaform</div>
  <div class="brand-tag">FARGE &amp; INTERIØRDESIGN</div>
</div>
<div class="abs hero-title">Farge &amp;<br>InteriørDesign</div>
<div class="abs btn hero-btn">Explore more</div>
<div class="abs dots"><span class="on"></span><span></span><span></span></div>

<div class="abs welcome-script">Welcome</div>
<h1 class="abs heading welcome-heading">TRENGER DU HJELP TIL UTVIKLING AV INTERIØRMILJØER?</h1>
<p class="abs body-text welcome-text">Lumaform AS jobber med utvikling av interiørmiljøer for private, bedrifter og offentlige institusjoner. Vi tilbyr alt fra fargevalg og møblering til komplette løsninger, enten det er et nytt eller eldre bygg. Sammen finner vi uttrykket som passer deg og ditt rom.</p>
<div class="abs btn welcome-btn">Read more</div>

<div class="abs private-panel"></div>
<div class="abs private-photo" role="img" aria-label="Stue med lys sofa, puter i oransje og hylle på veggen"></div>
<svg class="abs" style="left:540px;top:1180px" width="640" height="600" aria-hidden="true">
  <polyline points="10,580 10,120 300,10 610,120 610,580" fill="none" stroke="var(--line)" stroke-width="2"/>
</svg>
<h2 class="abs heading private-heading">PRIVATE INTERIØR</h2>
<p class="abs body-text private-text">Trenger du veiledning i forhold til farger, tekstiler eller innredning? Ønsker du hjelp til å skape et helhetlig hjem? Kanskje du har et gammelt hus som du skal renovere, eller et nytt hjem som skal innredes? Vi hjelper deg gjennom hele prosessen, fra første møte til ferdig resultat.</p>
<div class="abs btn private-btn">Explore more</div>

<div class="abs biz-band"></div>
<div class="abs biz-photo" role="img" aria-label="Kontor med betongvegg, arbeidsbord, stoler og stor plante"></div>
<svg class="abs" style="left:90px;top:1900px" width="600" height="580" aria-hidden="true">
  <polyline points="10,570 10,120 290,10 580,120 580,570 10,570" fill="none" stroke="var(--line)" stroke-width="2"/>
</svg>
<h2 class="abs heading biz-heading">BEDRIFT/OFFENTLIG</h2>
<p class="abs body-text biz-text">Lumaform hjelper deg med fargevalg, møbler og materialer i forbindelse med kontorer, butikker, skoler og institusjoner. Vi kan utarbeide tegninger, romplaner og komplette forslag til nye løsninger. Vi har lang erfaring med offentlige anskaffelser og legger vekt på et funksjonelt og vakkert arbeidsmiljø for alle.</p>
<div class="abs btn biz-btn">Explore more</div>

<div class="abs testi-band"></div>
<div class="abs testi-photo" role="img" aria-label="Lys stue med grå lenestol, taklampe og planter"></div>
<div class="abs quote-mark" aria-hidden="true">“</div>
<h2 class="abs heading testi-heading">CLIENT TESTIMONIALS</h2>
<p class="abs testi-text">“ Ragna forsto raskt hva vi ønsket oss, og resultatet ble bedre enn vi hadde forestilt oss. Hjemmet vårt føles nå både lyst, rolig og personlig. Vi anbefaler Lumaform på det varmeste. ”</p>
<div class="abs avatar" role="img" aria-label="Portrett av kunden"></div>
<div class="abs client-name">EIRIK HOLMSEN</div>
<div class="abs client-role">Kunde, privat bolig</div>
<div class="abs arrows" aria-hidden="true">
  <svg width="22" height="22"><circle cx="11" cy="11" r="10" fill="none" stroke="#9a9090"/><polyline points="13,6 8,11 13,16" fill="none" stroke="#9a9090" stroke-width="1.5"/></svg>
  <svg width="22" height="22"><circle cx="11" cy="11" r="10" fill="none" stroke="#9a9090"/><polyline points="9,6 14,11 9,16" fill="none" stroke="#9a9090" stroke-width="1.5"/></svg>
</div>

<div class="abs footer-brand">
  <div class="brand-mark"></div>
  <div class="brand-name">Lumaform</div>
  <div class="brand-tag">FARGE &amp; INTERIØRDESIGN</div>
</div>
<p class="abs body-text footer-about">Lumaform AS jobber med utvikling av interiørmiljøer for private, bedrifter og offentlige institusjoner.</p>

<div class="abs foot-col" style="left:448px">
  <div class="foot-title">QUICK LINKS</div>
  <ul class="foot-list">
    <li>Terms &amp; Conditions</li>
    <li>Sitemap</li>
    <li>Disclaimer</li>
    <li>Privacy Policy</li>
  </ul>
</div>

<div class="abs foot-col" style="left:620px">
  <div class="foot-title">EMAIL SIGN UP</div>
  <p class="foot-note">Meld deg på nyhetsbrevet vårt for inspirasjon og tilbud.</p>
  <div class="email-field">
    <svg width="16" height="12" aria-hidden="true"><rect x="0.5" y="0.5" width="15" height="11" fill="none" stroke="#8a8080"/><polyline points="0.5,0.5 8,7 15.5,0.5" fill="none" stroke="#8a8080"/></svg>
    Email address
  </div>
  <div class="signup-btn">SIGN UP</div>
</div>

<div class="abs foot-col" style="left:920px">
  <div class="foot-title">CONTACT US</div>
  <div class="contact-row">
    <svg width="14" height="18" aria-hidden="true"><path d="M7 1a5.5 5.5 0 0 0-5.5 5.5C1.5 11 7 17 7 17s5.5-6 5.5-10.5A5.5 5.5 0 0 0 7 1z" fill="none" stroke="#5b5050"/><circle cx="7" cy="6.5" r="2" fill="#5b5050"/></svg>
    <span>Fjordveien 8,<br>9990 Eksempelby</span>
  </div>
  <div class="contact-row">
    <svg width="14" height="16" aria-hidden="true"><path d="M3 1h3l1.5 4-2 1.5a9 9 0 0 0 4 4L11 8.5l3 1.5v3a2 2 0 0 1-2 2A12 12 0 0 1 1 3a2 2 0 0 1 2-2z" fill="none" stroke="#5b5050"/></svg>
    <span>+47 900 12 345</span>
  </div>
  <div class="contact-row">
    <svg width="16" height="12" aria-hidden="true"><rect x="0.5" y="0.5" width="15" height="11" fill="none" stroke="#5b5050"/><polyline points="0.5,0.5 8,7 15.5,0.5" fill="none" stroke="#5b5050"/></svg>
    <span>post@lumaform-example.no</span>
  </div>
</div>

<div class="abs bottom-bar"></div>
<div class="abs copyright">© Copyright 2021 Lumaform. All rights reserved.</div>
<div class="abs social" aria-label="Sosiale medier"><span></span><span></span><span></span><span></span></div>

</body>
</html>
```